Urgent - brand new business card for a startup technical advisory and incubation business in Sydney

We need a brand new business card design for BrightForge. We are a startup technical advisory and incubation business based in Sydney Australia. We work with entrepreneurs and innovators to help rapidly and efficiently turn their ideas into reality and to ensure they have the technical platform required for growth.

Our name is partly inspired by our love of lean product development methods and the lean startup movement.

We would like clean, uncluttered designs that feature our two logo colours and communicate a professional but creative, in-touch and entrepreneurial business.

PLEASE SEE MUST HAVE PRIORITIES FOR DRAFT CONTACT INFORMATION AND OTHER DESIRED TEXT ON CARD.
Updates

We have now updated the brief to include draft business card contact information and also some additional desired text to feature on the card design.    Please review the Must Have priorities.

Also final updated source files for the horizontal and vertical versions have now been uploaded and should be used for any designs.

Thanks!

Target Market(s)

Entrepeneurs, innovators, startup investors looking for a strong product development partner

Industry/Entity Type

Business

Requirements
Must have
• Feature our two logo colours
Be a relatively clean, pared back overall design - quite minimalist

Updated source files (AI) for vertical and horizontal layouts attached.

Draft contact information for business card:
Neil Barton
Founder & CTO
Phone: +61 427 555123
Email: xxxx@brightforge.com
Chatlink: xxxxxbarton
Chirper: nbarton

www.brightforge.com

We would also like the overall design to include the phrase "You have great ideas. Let us make them happen." (probably in a reasonably subtle way)

Nice to have
• Inspire me! Double-sided designs are fine with logo, phrase, (URL?) on one side and contact details on other (+ any other design elements)

Logo on business card can be either with lightbulb above the wording as per example here or to the left of the BrightForge wording - both layouts in files provided.
Should not have
• Shouldn't look like a Pentara Suite business card template :-)

```html
<!DOCTYPE html>
<html lang="en">
<head>
<meta charset="utf-8">
<title>BrightForge business card concepts</title>
<link rel="stylesheet" href="https://fonts.googleapis.com/css2?family=Jost:wght@400;500;700&family=Arimo:wght@400;700&family=Open+Sans:wght@400&display=swap">
<style>
  :root {
    --brand-blue: #1aa3dc;
    --brand-slate: #3b4450;
    --card-light: #f4f4f4;
    --card-mid: #e6e6e6;
    --card-dark: #d8d8d8;
    --text-dark: #2e2e2e;
    --heading: #333333;
    --swoosh-white: #ffffff;
    --swoosh-grey: #cfcfcf;
    --watermark: rgba(150,160,170,0.28);
    --page: #ffffff;
  }
  * { box-sizing: border-box; margin: 0; padding: 0; }
  html, body { width: 1200px; height: 1000px; overflow: hidden; background: var(--page); }
  .sheet { position: relative; width: 1200px; height: 1000px; }

  .section-heading {
    position: absolute;
    font-family: "Open Sans", Arial, sans-serif;
    font-weight: 400;
    font-size: 30px;
    color: var(--heading);
    transform: translateX(-50%);
    white-space: nowrap;
  }

  .card {
    position: absolute;
    width: 541px;
    height: 300px;
    border-radius: 72px 0 72px 0;
    overflow: hidden;
    background: linear-gradient(100deg, var(--card-light) 0%, var(--card-mid) 55%, var(--card-dark) 100%);
  }
  .card-swoosh { position: absolute; inset: 0; width: 100%; height: 100%; }

  .brand-mark {
    position: absolute;
    border-radius: 50%;
    background: radial-gradient(circle, #7fcdf0 0%, #b8e2f5 70%, rgba(184,226,245,0) 100%);
  }
  .brand-name {
    position: absolute;
    font-family: "Jost", Arial, sans-serif;
    font-weight: 500;
    color: var(--brand-blue);
    line-height: 1;
    white-space: nowrap;
  }
  .brand-tagline {
    position: absolute;
    font-family: "Arimo", Arial, sans-serif;
    font-weight: 700;
    color: var(--text-dark);
    white-space: nowrap;
  }

  .person {
    position: absolute;
    display: flex;
    flex-direction: column;
    align-items: flex-end;
  }
  .person-name {
    font-family: "Jost", Arial, sans-serif;
    font-weight: 700;
    line-height: 1;
    white-space: nowrap;
  }
  .person-name .first { color: var(--brand-blue); }
  .person-name .last { color: var(--brand-slate); }
  .person-role {
    font-family: "Jost", Arial, sans-serif;
    font-weight: 400;
    color: var(--brand-slate);
    text-transform: uppercase;
    white-space: nowrap;
  }

  .contact {
    position: absolute;
    list-style: none;
    font-family: "Arimo", Arial, sans-serif;
    color: var(--text-dark);
    white-space: nowrap;
  }

  .person--small .person-name { font-size: 32px; }
  .person--small .person-role { font-size: 8px; letter-spacing: 2.2px; margin-top: -5px; }
  .person--large .person-name { font-size: 47px; }
  .person--large .person-role { font-size: 10.5px; letter-spacing: 3.4px; margin-top: -7px; }
  .contact--small { font-size: 13px; line-height: 16px; }
  .contact--large { font-size: 18px; line-height: 21px; }

  .watermark-mark {
    position: absolute;
    border-radius: 50%;
    background: radial-gradient(circle, rgba(130,205,240,0.35) 0%, rgba(130,205,240,0.15) 65%, rgba(130,205,240,0) 100%);
  }
  .watermark-name {
    position: absolute;
    font-family: "Jost", Arial, sans-serif;
    font-weight: 500;
    font-size: 52px;
    line-height: 1;
    color: var(--watermark);
    white-space: nowrap;
  }
</style>
</head>
<body>
<div class="sheet">

  <h2 class="section-heading" style="left:370px; top:124px;">1 side version</h2>
  <h2 class="section-heading" style="left:940px; top:124px;">2 side version/front</h2>
  <h2 class="section-heading" style="left:611px; top:513px;">2 versions/back</h2>

  <!-- One-sided card -->
  <article class="card card--single" style="left:43px; top:178px;">
    <svg class="card-swoosh" viewBox="0 0 541 300" preserveAspectRatio="none" aria-hidden="true">
      <path d="M0 300 C120 200 300 140 541 130 L541 160 C330 170 160 220 40 300 Z" fill="var(--swoosh-white)" opacity="0.7"/>
      <path d="M0 250 C140 180 330 150 541 150" fill="none" stroke="var(--swoosh-grey)" stroke-width="6" opacity="0.6"/>
      <path d="M120 300 C240 220 400 185 541 175 L541 300 Z" fill="var(--swoosh-white)" opacity="0.35"/>
    </svg>
    <div class="brand-mark" role="img" aria-label="BrightForge symbol area" style="left:62px; top:20px; width:76px; height:76px;"></div>
    <div class="brand-name" style="left:17px; top:132px; font-size:32px;">BrightForge</div>
    <div class="brand-tagline" style="left:17px; top:171px; font-size:6.5px;">Bold ideas deserve a builder. We turn them real</div>
    <div class="person person--small" style="right:38px; top:172px;">
      <div class="person-name"><span class="first">Neil</span> <span class="last">Barton</span></div>
      <div class="person-role">Founder &amp; CTO</div>
    </div>
    <ul class="contact contact--small" style="left:319px; top:226px;">
      <li>Phone: +61 427 555123</li>
      <li>Email: xxxx@brightforge.com</li>
      <li>Chatlink: xxxxxbarton</li>
      <li>Chirper: nbarton</li>
    </ul>
  </article>

  <!-- Two-sided card, front -->
  <article class="card card--front" style="left:614px; top:178px;">
    <svg class="card-swoosh" viewBox="0 0 541 300" preserveAspectRatio="none" aria-hidden="true">
      <path d="M0 300 C120 200 300 140 541 130 L541 160 C330 170 160 220 40 300 Z" fill="var(--swoosh-white)" opacity="0.7"/>
      <path d="M0 250 C140 180 330 150 541 150" fill="none" stroke="var(--swoosh-grey)" stroke-width="6" opacity="0.6"/>
      <path d="M120 300 C240 220 400 185 541 175 L541 300 Z" fill="var(--swoosh-white)" opacity="0.35"/>
    </svg>
    <div class="brand-mark" role="img" aria-label="BrightForge symbol area" style="left:30px; top:30px; width:96px; height:96px;"></div>
    <div class="brand-name" style="left:141px; top:56px; font-size:38px;">BrightForge</div>
    <div class="brand-tagline" style="left:142px; top:112px; font-size:7.5px;">Bold ideas deserve a builder. We turn them real</div>
    <div class="person person--small" style="right:52px; top:233px;">
      <div class="person-name"><span class="first">Neil</span> <span class="last">Barton</span></div>
      <div class="person-role">Founder &amp; CTO</div>
    </div>
  </article>

  <!-- Back, plain -->
  <article class="card card--back" style="left:43px; top:570px;">
    <svg class="card-swoosh" viewBox="0 0 541 300" preserveAspectRatio="none" aria-hidden="true">
      <path d="M0 300 C120 200 300 140 541 130 L541 160 C330 170 160 220 40 300 Z" fill="var(--swoosh-white)" opacity="0.7"/>
      <path d="M0 250 C140 180 330 150 541 150" fill="none" stroke="var(--swoosh-grey)" stroke-width="6" opacity="0.6"/>
      <path d="M120 300 C240 220 400 185 541 175 L541 300 Z" fill="var(--swoosh-white)" opacity="0.35"/>
    </svg>
    <div class="person person--large" style="right:122px; top:72px;">
      <div class="person-name"><span class="first">Neil</span> <span class="last">Barton</span></div>
      <div class="person-role">Founder &amp; CTO</div>
    </div>
    <ul class="contact contact--large" style="left:166px; top:148px;">
      <li>Phone: +61 427 555123</li>
      <li>Email: xxxx@brightforge.com</li>
      <li>Chatlink: xxxxxbarton</li>
      <li>Chirper: nbarton</li>
    </ul>
  </article>

  <!-- Back, with faint brand -->
  <article class="card card--back-brand" style="left:617px; top:570px;">
    <svg class="card-swoosh" viewBox="0 0 541 300" preserveAspectRatio="none" aria-hidden="true">
      <path d="M0 300 C120 200 300 140 541 130 L541 160 C330 170 160 220 40 300 Z" fill="var(--swoosh-white)" opacity="0.7"/>
      <path d="M0 250 C140 180 330 150 541 150" fill="none" stroke="var(--swoosh-grey)" stroke-width="6" opacity="0.6"/>
      <path d="M120 300 C240 220 400 185 541 175 L541 300 Z" fill="var(--swoosh-white)" opacity="0.35"/>
    </svg>
    <div class="watermark-mark" role="img" aria-label="Faint BrightForge symbol area" style="left:55px; top:70px; width:130px; height:130px;"></div>
    <div class="watermark-name" style="right:26px; top:238px;">BrightForge</div>
    <div class="person person--large" style="right:122px; top:72px;">
      <div class="person-name"><span class="first">Neil</span> <span class="last">Barton</span></div>
      <div class="person-role">Founder &amp; CTO</div>
    </div>
    <ul class="contact contact--large" style="left:166px; top:148px;">
      <li>Phone: +61 427 555123</li>
      <li>Email: xxxx@brightforge.com</li>
      <li>Chatlink: xxxxxbarton</li>
      <li>Chirper: nbarton</li>
    </ul>
  </article>

</div>
</body>
</html>
```